Orbin Vale Systems

Our company is about IT hardwares and IT solutions. IT hardware such as PC, RAMS, storage and servers. IT solutions such as project management, BA. We are also selling new technology too.

Target Market(s)

Consumer, Small to Medium Business, Corporate

Requirements
Must have
• The business card must have the following:
• Name:
• Title:
• Contact Number:
• Email address:
• Website:
• Color: Must match the logo color upgrade

```html
<!DOCTYPE html>
<html lang="en">
<head>
<meta charset="utf-8">
<title>Orbin Vale Systems — Business Card</title>
<link rel="stylesheet" href="https://fonts.googleapis.com/css2?family=Arimo:wght@400;700&display=swap">
<style>
  :root {
    --stage: #2b2b2b;
    --card: #f7f7f7;
    --ink: #3a3a3a;
    --ink-soft: #555555;
    --amber: #c8892f;
    --amber-text: #d7861f;
    --band: #3d3d3d;
    --white: #ffffff;
  }
  * { box-sizing: border-box; margin: 0; padding: 0; }
  html, body { width: 1200px; height: 997px; overflow: hidden; }
  body {
    background: var(--stage);
    font-family: "Arimo", Arial, sans-serif;
    position: relative;
  }
  .card {
    position: absolute;
    left: 330px;
    width: 540px;
    height: 308px;
    background: var(--card);
    box-shadow: 0 14px 40px rgba(0,0,0,.55);
    overflow: hidden;
  }
  .card--front { top: 110px; }
  .card--back  { top: 540px; }
  .card__bands { position: absolute; inset: 0; width: 100%; height: 100%; }

  .brand { position: absolute; display: flex; align-items: center; gap: 12px; }
  .brand__mark { width: 20px; height: 20px; background: var(--amber); }
  .brand__name {
    font-weight: 700;
    color: var(--ink);
    letter-spacing: 1px;
    text-transform: uppercase;
    white-space: nowrap;
  }
  .card--front .brand { left: 0; right: 0; top: 110px; justify-content: center; }
  .card--front .brand__name { font-size: 34px; }
  .card--back .brand { right: 36px; top: 172px; }
  .card--back .brand__name { font-size: 24px; }
  .card--back .brand__mark { width: 16px; height: 16px; }

  .person { position: absolute; left: 40px; top: 44px; }
  .person__name { font-size: 19px; color: var(--amber-text); }
  .person__title { font-size: 12px; color: var(--ink-soft); margin-top: 2px; }

  .contact { position: absolute; left: 44px; top: 196px; list-style: none; }
  .contact__item { font-size: 13px; color: var(--ink-soft); height: 34px; line-height: 34px; }

  .icon-rail {
    position: absolute; left: 0; top: 196px;
    width: 30px; height: 70px;
    background: var(--band);
    border-radius: 0 6px 6px 0;
    display: flex; flex-direction: column; align-items: center; justify-content: space-around;
    padding: 6px 0;
  }
  .icon-rail svg { width: 14px; height: 14px; }

  .website {
    position: absolute; right: 26px; top: 252px;
    font-size: 12px; font-weight: 700; color: var(--white);
  }
</style>
</head>
<body>

  <section class="card card--front" aria-label="Card front">
    <svg class="card__bands" viewBox="0 0 540 308" preserveAspectRatio="none" aria-hidden="true">
      <path d="M0 300 L330 280 C350 279 356 266 372 262 L540 252 L540 308 L0 308 Z" fill="var(--band)"/>
      <path d="M0 298 L360 276 L360 282 L0 306 Z" fill="var(--amber)"/>
      <rect x="0" y="300" width="540" height="8" fill="var(--amber)"/>
    </svg>
    <div class="brand">
      <span class="brand__mark"></span>
      <span class="brand__name">Orbin Vale Systems</span>
    </div>
  </section>

  <section class="card card--back" aria-label="Card back">
    <svg class="card__bands" viewBox="0 0 540 308" preserveAspectRatio="none" aria-hidden="true">
      <path d="M300 290 C320 288 322 246 346 244 L540 236 L540 308 L300 308 Z" fill="var(--band)"/>
      <path d="M0 294 L330 276 C318 284 316 290 312 296 L0 308 Z" fill="var(--amber)"/>
      <rect x="0" y="300" width="540" height="8" fill="var(--amber)"/>
    </svg>

    <div class="person">
      <p class="person__name">Marisol T Reyes</p>
      <p class="person__title">Managing Partner</p>
    </div>

    <div class="icon-rail" aria-hidden="true">
      <svg viewBox="0 0 16 16"><path d="M4 1h8v4H4z M2 6h12v6h-2v3H4v-3H2z" fill="var(--white)"/><rect x="5" y="10" width="6" height="4" fill="var(--band)"/></svg>
      <svg viewBox="0 0 16 16"><rect x="1" y="3" width="14" height="10" fill="var(--white)"/><path d="M1 3 L8 9 L15 3" fill="none" stroke="var(--band)" stroke-width="1.4"/></svg>
    </div>
    <ul class="contact">
      <li class="contact__item">+1 (555) 014-2290</li>
      <li class="contact__item">marisol@orbinvalesys.com</li>
    </ul>

    <div class="brand">
      <span class="brand__mark"></span>
      <span class="brand__name">Orbin Vale Systems</span>
    </div>

    <p class="website">www.orbinvalesys.com</p>
  </section>

</body>
</html>
```